New Custom Pizza Box Design Project For Independant Restaurant

We are looking for creative designs for our new custom printed pizza boxes. Designs should include the following:

-Our logo & company name
-A color scheme similar to our current logo
-Our physical and URL addresses & phone number (menu is attached)
-Ability to scale the design across several box sizes (10x10x2, 14x14x2, 18x13x2,
26x18x2)
- Any creative flair you think will make for the best design

Design can be on a white or kraft (tan) box.
Designs can be either two or three ink colors.

***Please note, designs must be able to be screen printed on boxes***
Updates

Reason: Still debating which to choose

Target Market(s)

Industry/Entity Type

Pizza Delivery

Font styles to use
Other font styles liked:
• Please use font similar to our logo text

Requirements
Must have
• -2 or 3 ink colors
• -company name, address, phone number, URL
• -company logo and colors
• -flexibility to use on different box sizes (10x10x2, 14x14x2, 18x13x2,
• 26x18x2)
• -utilize full printable area on boxes (including 2" dimension on box sides)
• ***Please note, designs must be able to be screen printed on boxes***
Should not have
• Design features with strong similarities to existing designs of other pizzerias

```html
<!DOCTYPE html>
<html lang="en">
<head>
<meta charset="utf-8">
<title>Marco's Henhouse &amp; Pizzeria – Box Lid</title>
<link rel="stylesheet" href="https://fonts.googleapis.com/css2?family=Oswald:wght@500;600&display=swap">
<style>
  :root {
    --mustard: #e6b51a;
    --bark: #5d3a27;
    --stitch: #3a2718;
    --cream: #ffffff;
  }
  html, body {
    margin: 0;
    padding: 0;
    overflow: hidden;
  }
  .box-lid {
    position: relative;
    width: 1200px;
    height: 1200px;
    background: var(--mustard);
    overflow: hidden;
    font-family: "Oswald", sans-serif;
  }
  .ribbon {
    position: absolute;
    inset: 0;
  }
  .brand {
    position: absolute;
    left: 356px;
    width: 563px;
    top: 290px;
    text-align: center;
    color: var(--cream);
    font-weight: 500;
    text-transform: uppercase;
    line-height: 1.05;
  }
  .brand__owner { font-size: 62px; letter-spacing: 2px; }
  .brand__name { font-size: 92px; letter-spacing: 3px; }
  .brand__trade { font-size: 58px; letter-spacing: 3px; margin-top: 14px; }
  .contact {
    position: absolute;
    left: 0;
    right: 0;
    top: 1010px;
    text-align: center;
    line-height: 1.1;
  }
  .contact__web {
    font-size: 56px;
    font-weight: 600;
    color: var(--bark);
    letter-spacing: 1px;
    text-shadow: 0 2px 3px rgba(0,0,0,0.35);
  }
  .contact__phone {
    font-size: 52px;
    font-weight: 500;
    color: var(--cream);
    text-shadow: 0 2px 3px rgba(0,0,0,0.35);
  }
</style>
</head>
<body>
  <main class="box-lid">
    <svg class="ribbon" width="1200" height="1200" viewBox="0 0 1200 1200" aria-hidden="true">
      <polygon points="356,0 919,0 919,936 634,810 356,936" fill="var(--bark)"/>
      <g fill="none" stroke="var(--stitch)" stroke-width="2.5" stroke-dasharray="9 5">
        <polyline points="340,0 340,974 634,828 937,974 937,0"/>
        <polyline points="347,0 347,968 634,836 930,968 930,0"/>
      </g>
    </svg>

    <div class="brand">
      <div class="brand__owner">Marco's</div>
      <div class="brand__name">Henhouse</div>
      <div class="brand__trade">&amp; Pizzeria</div>
    </div>

    <div class="contact">
      <div class="contact__web">WWW.HENHOUSEPIZZA.COM</div>
      <div class="contact__phone">Call us on +01 555 0192</div>
    </div>
  </main>
</body>
</html>
```